Slick Web Design for Health Care Software Company

We need a new corporate web design for our company, "Brivora." We specialize in web-based cloud software geared toward helping health care professionals.

Our focus for our home site is our products and services. We want potential clients and medical boards who visit our site to have an immediate sense of professionalism and know-how. Our products are innovative, easy to use, and customizable. Users should get this feel when visiting our site.

This is a link to our previous site: www.brivorainc.example. This site is too busy, the colors are too dark, and there's too much information in each page. When creating a design, feel free to eliminate the plethora of info present in the old site.

We have a logo and content for our site that we're going to use. For each of the 7-10 products and services, there is going to be a short 1-2 paragraph excerpt on their own page, as well as a case study related to each. Other parts that can be integrated into the site are our portfolio of clients, newsletter, and about us/contact us.

Some websites to use as general inspiration:
http://www.quellsite.example/
http://www.vantrex.example/
http://www.telmaroplans.example/

Target Market(s)

Health Care Professionals from Specialty Organizations and Boards

Industry/Entity Type

Health Care

Requirements
Nice to have
• Our trademark slogan is "Turn data in knowledge, knowledge into improvement." It would be pretty sweet to integrate this idea into the design of the site.

Also, BE CREATIVE. AVOID TRADITIONAL DESIGNS. Try to exemplify innovation within clarity.
Should not have
• Avoid dark backgrounds.

```html
<!DOCTYPE html>
<html lang="en">
<head>
<meta charset="utf-8">
<title>QMI Tallyst / VP Systems – Brivora</title>
<link href="https://fonts.googleapis.com/css2?family=Open+Sans:wght@400;600;700&family=Ubuntu:wght@400;500;700&display=swap" rel="stylesheet">
<style>
:root{
  --ink:#111;
  --text:#2b2b2b;
  --muted:#9a9a9a;
  --rule:#c9c9cc;
  --accent:#f2e600;
  --frame:#050505;
  --btn-top:#7b6f8c;
  --btn-bottom:#4c4259;
  --bg-top:#e9eaef;
  --bg-bottom:#e4e4e9;
  --screen-light:#e6eaf1;
  --screen-blue:#1f3d74;
}
*{margin:0;padding:0;box-sizing:border-box}
html,body{width:1031px;height:1200px;overflow:hidden}
body{font-family:"Open Sans",sans-serif;color:var(--text);
  background:linear-gradient(to bottom,var(--bg-top) 0,#fff 130px,#fff 1050px,var(--bg-bottom) 1200px)}
a{text-decoration:none}
.page{position:relative;width:1031px;height:1200px}

.brand{position:absolute;left:89px;top:28px;display:flex;align-items:center;gap:8px}
.brand-mark{width:26px;height:26px;border-radius:50%;background:var(--accent)}
.brand-name{font-family:"Ubuntu",sans-serif;font-weight:500;font-size:30px;color:var(--ink);letter-spacing:-.5px}

.main-nav{position:absolute;right:89px;top:42px;display:flex;gap:22px;font-family:"Ubuntu",sans-serif;font-size:14px;color:var(--ink)}
.main-nav a{color:inherit;padding-bottom:4px}
.main-nav a.current{border-bottom:3px solid var(--accent)}
.header-rule{position:absolute;left:89px;top:92px;width:853px;border-top:1px solid var(--rule)}

.side-nav{position:absolute;left:89px;top:138px;width:169px;height:878px;
  border-right:2px solid #d8d8d8;
  background:linear-gradient(to right,rgba(255,255,255,0) 40%,#f0f0f0)}
.side-nav a{position:absolute;left:0;width:171px;font-size:11.5px;line-height:15px;color:var(--muted)}
.side-nav a.current{color:var(--ink);background:#fff;top:216px;height:47px;padding-top:14px}

.page-title{position:absolute;left:302px;top:124px;font-size:42px;font-weight:700;color:var(--ink);letter-spacing:-.5px}

.showcase{position:absolute;left:302px;top:220px;width:640px;height:383px;background:var(--frame);border-radius:16px}
.showcase-screen{position:absolute;left:27px;top:27px;width:587px;height:329px;
  background:linear-gradient(to bottom,var(--screen-light) 0,var(--screen-light) 22%,var(--screen-blue) 23%,#2f4f88 52%,var(--screen-light) 53%,var(--screen-light) 100%)}

.tabs{position:absolute;left:302px;top:669px;width:640px;height:37px;border-bottom:1px solid #999;
  background:linear-gradient(to bottom,#fff,#f1f1f1)}
.tab{position:absolute;top:0;height:37px;display:flex;align-items:center;gap:5px;font-size:12px;font-weight:600}
.tab-active{left:0;width:126px;justify-content:center;background:#fff;border-top:3px solid var(--accent);
  border-left:1px solid #999;border-right:1px solid #999;height:38px;color:var(--ink)}
.tab-idle{left:149px;color:#888}

.description{position:absolute;left:302px;top:722px;width:642px;font-size:14.2px;line-height:24px;color:var(--text)}
.description p+p{margin-top:21px}

.cta{position:absolute;left:702px;top:963px;width:240px;height:48px;border-radius:4px;
  background:linear-gradient(to bottom,var(--btn-top),var(--btn-bottom));
  box-shadow:0 4px 6px rgba(0,0,0,.25);
  display:flex;align-items:center;justify-content:center;gap:8px;
  font-family:"Ubuntu",sans-serif;font-weight:700;font-size:16.5px;color:#fff}

.footer-rule{position:absolute;left:89px;top:1106px;width:853px;border-top:1px solid var(--rule)}
.footer-info{position:absolute;left:89px;top:1124px;font-family:"Ubuntu",sans-serif;font-size:11.5px;line-height:17px;color:var(--ink)}
.footer-info .copy{font-size:10px;margin-top:5px;color:#333}
.newsletter{position:absolute;left:716px;top:1129px;width:226px;height:28px;border:1px solid #aaa;border-radius:3px;background:#fff;
  font-family:"Ubuntu",sans-serif;font-size:11.5px;color:#aaa;display:flex;align-items:center;justify-content:space-between;padding:0 10px}
.social{position:absolute;right:89px;top:1164px;display:flex;gap:5px}
.social span{width:14px;height:14px;border-radius:2px;background:#777}
.social span:last-child{background:#aaa}
</style>
</head>
<body>
<div class="page">
  <header>
    <div class="brand"><span class="brand-mark"></span><span class="brand-name">Brivora</span></div>
    <nav class="main-nav">
      <a href="#">About Us</a>
      <a href="#">Services</a>
      <a href="#" class="current">Products</a>
      <a href="#">Resources</a>
      <a href="#">Contact Us</a>
    </nav>
    <div class="header-rule"></div>
  </header>

  <nav class="side-nav">
    <a href="#" style="top:15px">Online Learning / CME</a>
    <a href="#" style="top:61px">QMI Tallyst / PI Platform<br>for Custom PI CME</a>
    <a href="#" style="top:122px">QMI Registry / PQRS Registry</a>
    <a href="#" style="top:169px">QMI Tallyst / SAM<br>Self-Assessmentg</a>
    <a href="#" class="current">QMI Tallyst / VP Systems</a>
    <a href="#" style="top:276px">CE Program Evaluations</a>
    <a href="#" style="top:322px">Patient &amp; Peer Surveys</a>
    <a href="#" style="top:369px">Quality Improvement<br>Systems and Practice<br>Assessment</a>
    <a href="#" style="top:445px">QMI Outcome Tracker</a>
    <a href="#" style="top:491px">QMI Corvane Learning<br>Management System</a>
    <a href="#" style="top:553px">Content Managed Websites<br>and Systems</a>
  </nav>

  <h1 class="page-title">QMI Tallyst / VP Systems</h1>

  <div class="showcase">
    <div class="showcase-screen" role="img" aria-label="Screenshot of a client continuing-education portal with a health banner and content columns"></div>
  </div>

  <div class="tabs">
    <div class="tab tab-active">
      <svg width="12" height="12" viewBox="0 0 12 12"><circle cx="6" cy="6" r="4.5" fill="none" stroke="#111" stroke-width="3" stroke-dasharray="2 1.5"/><circle cx="6" cy="6" r="1.5" fill="#fff"/></svg>
      Description
    </div>
    <div class="tab tab-idle">
      <svg width="13" height="13" viewBox="0 0 13 13"><circle cx="6.5" cy="4" r="3" fill="#888"/><path d="M1 13c0-4 2.5-5.5 5.5-5.5S12 9 12 13z" fill="#888"/></svg>
      Case Studies
    </div>
  </div>

  <div class="description">
    <p>Lorem ipsum dolor sit amet, consectetur adipiscing elit. Phasellus vel dolor eros. Proin bibendu mcondimentum tincidunt. Nullam eget pellentesque nisl. Donec quis elit tellus, eu sollicitudin mi. Suspendisse vel eros nulla, in egestas augue. Suspendisse at eros nec ligula condimentum laoreet. Praegsent tincidunt iaculis lectus in ultrices. Aliquam sapien est, imperdiet at auctorac.</p>
    <p>Accumsan elementum nisi. Morbi consectetur ligula quis est aliquet sit amet blandit elit sagittis. Ut vel ipsum nisi, ac placerat purus. Aenean mi risus, placerat at mattis sit amet, suscipit et sapi. Maecenas eu lectus purus. Donec in orci non nibh gravida rutrum. In eget turpis elit. Aeneaneg et urna nisi. Vivamus vitae ligula nisl, quis ultricies quam. Aenean suscipit volutpat mattis.</p>
  </div>

  <a class="cta" href="#">
    <svg width="20" height="18" viewBox="0 0 20 18"><path d="M1 8h5l1 3h6l1-3h5v9H1z" fill="#fff"/><path d="M10 1v7M7 5l3 3 3-3" stroke="#fff" stroke-width="2" fill="none"/></svg>
    Contact us for details
  </a>

  <footer>
    <div class="footer-rule"></div>
    <div class="footer-info">
      <div>Brivora &nbsp;|&nbsp; 48 Harrow Mill Rd. Suite 12 Alderbrook, PA 19088</div>
      <div>Ph: 555.014.2280 &nbsp;|&nbsp; Email: info@brivorainc.example</div>
      <div class="copy">©2013 Brivora. All Rights Reserved.</div>
    </div>
    <div class="newsletter"><span>Join our newsletter</span><span>&gt;</span></div>
    <div class="social"><span></span><span></span><span></span><span></span><span></span><span></span></div>
  </footer>
</div>
</body>
</html>
```